Non-profit organization requires InDesign based template for a educational booklet

***Overview***
Our business "The Coastal Brightpath Centre for Skills and Learning" is a not for profit organisation working in vocational education both in the Australian and international markets. While we work within many professional contexts, we also work with projects in developing countries assisting to build institutional capacity in the education industry, upskilling in disadvantaged communities to ultimately facilitate positive development outcomes.

Our project is looking to deliver agricultural-based education units that will be delivered in booklet form. Vocational students will use these unit booklets for self-paced or classroom group study. The front of each unit will have a nice graphical cover page, contents and details about learning in the unit. This will be followed by about 15 pages of educational content with plenty of pictures and other material such as tables and graphs to illustrate learning points. This will then be followed by a short question sheet with space for students to write answers, followed by Activity sheets where students put into practice skills from the unit.

***The designed template should have***
* Cover page;
* Content page;
* Two (2) different introduction pages (two for variation);
* Three (3) different pages for lesson text – these pages will be the main study pages for the students, 3 for variation;
* Activity page - like an activity worksheet;
* Question page - page with questions or reflections that the students need to answer - a space under each question for students to write;

***Design preferences***

*Font – an inDesign default font please like Calibri – text built on a base Normal font 11pt, then headings H1, H2 etc... from that basis e.g. 24pt for H1 etc... the size up to the designer.

Happy to see creativity of graphic artists with the above themes.

Target Market(s)

In the requested project, I require an Adobe InDesign template (file in .indd) to be designed that will have particular characteristics suited to students who are:

* Age 15-17;
* Have the educational equivalent to Australian and US education standard of Yr 8;
* Attending vocational school - vocational schools are between secondary high school and University and are usually used to produce graduates within the skill trade area;
* Agricultural theme in the template;
* Sustainability theme (agricultural sustainability) as well;

Students are from very poor rural farming families in growing rice, coconut, rambutan, mangoes, cocoa, palm oil... - very SE Asian agricultural landscape.

Students are used to black and white government textbooks which are very dry, largely dull in design and colour – we do not want this!

Industry/Entity Type

Agriculture

Font styles to use
Sans Serif

Colors

Designer to choose colors to be used in the design.

Requirements
Must have
• * Final file must be in an editable Adobe Indesign file (.indd), with editable layers;
• * SE Asian agricultural theme in the template;
• * design must not look like dull and boring textbooks or corporate training booklets; * design should be vibrant and interesting but also not distracting from the lesson (i.e. it is not too garish);
• * suitable colours (it will be printed full colour) easy on the eye for students of the age group - colours related to agriculture;
• *Modern look and feel;
Should not have
• * design must not look like dull and boring textbooks or corporate training booklets;

```html
<!DOCTYPE html>
<html lang="en">
<head>
<meta charset="utf-8">
<title>Agricultural Education – Unit Booklet Cover</title>
<link rel="stylesheet" href="https://fonts.googleapis.com/css2?family=Montserrat:wght@500&family=Open+Sans:ital,wght@1,300;1,800&display=swap">
<style>
  :root {
    --backdrop: #b8b9bb;
    --paper: #ffffff;
    --brand-blue: #0a6aad;
    --leaf-green: #7aab3e;
    --ink: #1a1a1a;
    --field-green: #7f9c4a;
    --field-green-deep: #4f6e2c;
    --herd-brown: #a8622a;
    --herd-brown-deep: #6e3a17;
  }
  * { margin: 0; padding: 0; box-sizing: border-box; }
  html, body {
    width: 1200px;
    height: 1200px;
    overflow: hidden;
    background: var(--backdrop);
  }
  .cover-canvas { display: block; width: 1200px; height: 1200px; }
  .org-name {
    font-family: "Montserrat", sans-serif;
    font-weight: 500;
    font-size: 22px;
    fill: var(--paper);
  }
  .unit-label {
    font-family: "Open Sans", sans-serif;
    font-style: italic;
    font-weight: 300;
    font-size: 54px;
    letter-spacing: 2px;
    fill: var(--ink);
  }
  .unit-title {
    font-family: "Open Sans", sans-serif;
    font-style: italic;
    font-weight: 800;
    font-size: 64px;
    letter-spacing: 2px;
    fill: var(--paper);
  }
</style>
</head>
<body>
<svg class="cover-canvas" viewBox="0 0 1500 1500" xmlns="http://www.w3.org/2000/svg">
  <defs>
    <linearGradient id="herd-tone" x1="0" y1="0" x2="0.3" y2="1">
      <stop offset="0" stop-color="#5a3a22"/>
      <stop offset="0.45" stop-color="var(--herd-brown)"/>
      <stop offset="1" stop-color="var(--herd-brown-deep)"/>
    </linearGradient>
    <linearGradient id="field-tone" x1="0" y1="0" x2="1" y2="1">
      <stop offset="0" stop-color="var(--field-green)"/>
      <stop offset="1" stop-color="var(--field-green-deep)"/>
    </linearGradient>
    <filter id="title-shadow" x="-5%" y="-20%" width="110%" height="140%">
      <feDropShadow dx="2" dy="3" stdDeviation="3" flood-color="#000" flood-opacity="0.45"/>
    </filter>
  </defs>

  <!-- cover photography -->
  <g class="cover-photo" role="img" aria-label="Photograph: hairy green soybean pods on the left and a brown calf looking forward among a herd of cattle">
    <rect x="231" y="33" width="1014" height="1434" fill="url(#herd-tone)"/>
    <polygon points="231,33 580,33 231,1030" fill="url(#field-tone)"/>
  </g>

  <!-- large letter A frame -->
  <path class="letter-frame" fill="var(--paper)"
        d="M231,1030 L580,33 L793,33 L1105,905 L1245,905 L1245,1040 L1030,1040 Q995,1040 985,1000 L678,120 L231,1440 Z"/>
  <polygon class="letter-crossbar" fill="var(--paper)" points="480,650 760,650 785,760 442,760"/>

  <!-- brand panel -->
  <polygon class="brand-panel" fill="var(--brand-blue)" points="793,33 1245,33 1245,905 1105,905"/>
  <circle class="brand-dot" cx="1058" cy="130" r="34" fill="var(--paper)"/>
  <text class="org-name" text-anchor="middle">
    <tspan x="1058" y="215">The Coastal Brightpath</tspan>
    <tspan x="1058" y="245">Centre for Skills</tspan>
    <tspan x="1058" y="275">and Learning</tspan>
  </text>

  <!-- plus sign -->
  <g class="plus-sign">
    <rect x="806" y="514" width="62" height="247" rx="10" fill="var(--paper)"/>
    <rect x="722" y="609" width="234" height="57" rx="10" fill="var(--paper)"/>
    <rect x="812" y="520" width="50" height="235" rx="8" fill="var(--leaf-green)"/>
    <rect x="728" y="615" width="222" height="45" rx="8" fill="var(--leaf-green)"/>
  </g>

  <text class="unit-label" x="394" y="722">EDUCATION</text>
  <text class="unit-title" x="1185" y="1395" text-anchor="end" filter="url(#title-shadow)">AGRICULTURAL</text>
</svg>
</body>
</html>
```